Finance Product Agency Business Card Design

We're an agency that provides products (service contracts, gap insurance, tire and wheel, etc) and support to dealership finance departments. We specialize in training finance producers to maximize their potential and also keep them up to date on the ever changing compliance and legal landscape. I'll attach an image of our logo, excited to see what you all come up with. Would also be interested in discussing our new website design with the winner.

Target Market(s)

auto dealerships

Industry/Entity Type

Business

Contact Information for Business Card

Mark Dolvery
Phone 317.624.5583
Fax 855.472.3308
email Mark.Dolvery@brightlanecoverage.example

Requirements
Must have
• basic contact information
Nice to have
• looking for something professional but modern

```html
<!DOCTYPE html>
<html lang="en">
<head>
<meta charset="utf-8">
<title>Brightlane Coverage – Business Cards</title>
<link rel="stylesheet" href="https://fonts.googleapis.com/css2?family=Lato:ital,wght@0,300;0,400;0,700;0,900;1,300&display=swap">
<style>
  :root {
    --backdrop: #e9e9e7;
    --card-white: #ffffff;
    --band-dark: #2e2e2e;
    --band-mid: #4a4a4a;
    --band-light: #5e5e5e;
    --brand-teal: #2f6470;
    --ink: #3a3a3a;
    --ink-soft: #6a6a6a;
    --rule: #2f6470;
  }
  * { box-sizing: border-box; margin: 0; padding: 0; }
  html, body {
    width: 1200px; height: 800px; overflow: hidden;
    background: var(--backdrop);
    font-family: "Lato", Arial, sans-serif;
  }
  .canvas { position: relative; width: 1200px; height: 800px; }

  .card {
    position: absolute; top: 250px;
    width: 525px; height: 300px;
    background: var(--card-white);
    box-shadow: 0 6px 18px rgba(0,0,0,0.18);
    overflow: hidden;
  }
  .card--front { left: 50px; }
  .card--back { left: 625px; }

  .edge-band {
    position: absolute; top: 0; bottom: 0; width: 38px;
    background: repeating-linear-gradient(
      to bottom,
      var(--band-dark) 0 30px,
      var(--band-mid) 30px 60px,
      var(--band-light) 60px 90px,
      var(--band-mid) 90px 120px
    );
  }
  .edge-band--left { left: 0; }
  .edge-band--right { right: 0; }

  .brand {
    position: absolute; top: 0; bottom: 0;
    display: flex; align-items: center; justify-content: center;
    color: var(--brand-teal);
    font-weight: 900; text-transform: uppercase;
    white-space: nowrap;
  }
  .brand__dot {
    border-radius: 50%; background: var(--brand-teal); flex: none;
  }
  .card--front .brand {
    left: 38px; right: 38px;
    font-size: 27px; letter-spacing: 0.5px; gap: 12px;
    padding-bottom: 20px;
  }
  .card--front .brand__dot { width: 40px; height: 40px; }

  .contact-panel {
    position: absolute; left: 0; top: 0; bottom: 0; width: 255px;
    background: linear-gradient(to bottom, #f2f2f2, #e2e2e2);
    padding: 40px 20px 0 24px;
    color: var(--ink);
  }
  .contact-name {
    display: flex; align-items: center; gap: 8px;
    font-size: 21px; font-weight: 400; text-transform: uppercase; letter-spacing: 0.5px;
  }
  .contact-name svg { flex: none; }
  .contact-role {
    font-size: 17px; font-weight: 300; color: var(--ink-soft);
    margin: 2px 0 0 36px;
  }
  .rule { height: 1px; background: var(--rule); margin: 16px 0; }
  .contact-row {
    display: flex; align-items: center; gap: 12px;
    font-size: 11.5px; line-height: 1.5; color: var(--ink);
  }
  .contact-row svg { flex: none; }
  .contact-row--email { font-size: 9.5px; gap: 8px; }

  .card--back .brand {
    left: 255px; right: 38px;
    font-size: 14px; letter-spacing: 0.3px; gap: 7px;
    padding-bottom: 12px;
  }
  .card--back .brand__dot { width: 20px; height: 20px; }
</style>
</head>
<body>
<main class="canvas">

  <section class="card card--front" aria-label="Card front">
    <div class="edge-band edge-band--left"></div>
    <div class="brand"><span class="brand__dot"></span>Brightlane Coverage</div>
    <div class="edge-band edge-band--right"></div>
  </section>

  <section class="card card--back" aria-label="Card back">
    <div class="contact-panel">
      <h1 class="contact-name">
        <svg width="26" height="26" viewBox="0 0 26 26" aria-hidden="true">
          <circle cx="13" cy="13" r="12" fill="#4a4a4a"/>
          <circle cx="13" cy="10" r="4" fill="#fff"/>
          <path d="M6 21c1.5-4 4-5.5 7-5.5s5.5 1.5 7 5.5z" fill="#fff"/>
        </svg>
        Mark Dolvery
      </h1>
      <p class="contact-role">Creative Manager</p>
      <div class="rule"></div>
      <div class="contact-row">
        <svg width="22" height="22" viewBox="0 0 22 22" aria-hidden="true">
          <circle cx="11" cy="11" r="10" fill="#4a4a4a"/>
          <path d="M7.5 6.5l2 2-1 1.2c.6 1.3 1.6 2.3 2.9 2.9l1.2-1 2 2-1.2 1.4c-3.3-.4-6.1-3.2-6.5-6.5z" fill="#fff"/>
        </svg>
        <div>Phone: 317.624.5583<br>Fax: 855.472.3308</div>
      </div>
      <div class="rule"></div>
      <div class="contact-row contact-row--email">
        <svg width="22" height="22" viewBox="0 0 22 22" aria-hidden="true">
          <circle cx="11" cy="11" r="10" fill="#4a4a4a"/>
          <rect x="6" y="7.5" width="10" height="7" fill="none" stroke="#fff" stroke-width="1.2"/>
          <path d="M6 7.5l5 4 5-4" fill="none" stroke="#fff" stroke-width="1.2"/>
        </svg>
        Mark.Dolvery@brightlanecoverage.example
      </div>
    </div>
    <div class="brand"><span class="brand__dot"></span>Brightlane Coverage</div>
    <div class="edge-band edge-band--right"></div>
  </section>

</main>
</body>
</html>
```